BRINEWOLF STUDIOS Video/Photo for Wedding/Events

We need a web design including the code which will be ready to launch. we are a Video and photography company in New Zealand and focus on medium to large Weddings and events.
The site will be our main point of contact with our customers with no more than 4-5 pages (Home, Pricing, Photo/Video Gallery, Contact) and we would like to be able to change the content of all pages as needed. The photos will be uploaded to our website but the videos we can only put the YouTube link.
I will add our company logo and some photos we have already taken to give you an idea of our product and services and can be used in the site as well.

Our pricing section will have photos, videos and photos + videos in 3 different pricing plans which we can upload and change as we need.

Here are some web pages to give you an idea of our industry and our competitors sites, however we would like the quality and design of our work to be better than all of our competitors sites which are listed below.

http://www.tarvelmedia.example.nz/2012/02/9-great-new-zealand-photographers-websites/
http://kobphotography.example.uk/
http://www.marthequillonphotography.example.nz/

Target Market(s)

our target audience is medium to up market customers who are looking at booking their wedding video/photography as well as events

Industry/Entity Type

Industry

Requirements
Must have
• The page must have a minimum of 4 pages, however we would like the designers to look outside the box and be creative with their designs.
Nice to have
• similar colors to our logo but don't limit your self and keep an open mind.

```html
<!DOCTYPE html>
<html lang="en">
<head>
<meta charset="utf-8">
<title>Brinewolf Studios</title>
<link href="https://fonts.googleapis.com/css2?family=Josefin+Sans:wght@300;400&family=Arimo:wght@400;700&display=swap" rel="stylesheet">
<style>
:root{
  --ink:#0d0d0d;
  --panel:#1a1a1a;
  --teal:#4fb6c1;
  --teal-dark:#3a8f98;
  --white:#ffffff;
  --light-text:#e6e6e6;
  --logo-grey:#5a5a5a;
}
*{margin:0;padding:0;box-sizing:border-box}
html,body{width:1200px;height:930px;overflow:hidden;background:var(--ink)}
body{position:relative;font-family:"Arimo",Arial,sans-serif;color:var(--light-text)}
.hero{position:absolute;left:0;top:0;width:1200px;height:602px;
  background:linear-gradient(180deg,#141a10 0%,#252a1c 40%,#4a4838 70%,#6a6660 100%)}
.topbar{position:absolute;left:0;top:0;width:1200px;height:34px;background:rgba(8,8,8,.92);border-bottom:2px dotted var(--teal)}
.nav{position:absolute;left:266px;top:9px;display:flex;gap:13px;font-family:"Josefin Sans",sans-serif;font-weight:400;font-size:14px;letter-spacing:.4px;color:var(--white)}
.nav .sep{color:#ccc}
.social{position:absolute;right:10px;top:6px;display:flex;gap:3px}
.social i{display:block;width:20px;height:20px;border-radius:50%;border:1px solid #ccc;background:#2a2a2a}
.brand-panel{position:absolute;left:0;top:0;width:234px;height:230px}
.brand-shape{position:absolute;left:0;top:0}
.brand-dot{position:absolute;left:92px;top:50px;width:50px;height:50px;border-radius:50%;background:var(--teal)}
.brand-name{position:absolute;left:0;top:138px;width:234px;text-align:center;font-family:"Josefin Sans",sans-serif;font-weight:400;font-size:21px;letter-spacing:2px;color:var(--logo-grey);line-height:1.35}
.hero-title{position:absolute;right:97px;top:80px;text-align:right;font-family:"Josefin Sans",sans-serif;font-weight:300;color:var(--white);line-height:1}
.hero-title .main{font-size:64px;letter-spacing:2px}
.hero-title .sub{font-size:35px;margin-top:6px;letter-spacing:1px}
.arrow{position:absolute;top:346px}
.arrow.left{left:0}
.arrow.right{right:0}
.band{position:absolute;left:0;top:602px;width:1200px;height:4px;border-top:2px dotted var(--teal)}
.content{position:absolute;left:0;top:606px;width:1200px;height:285px;background:rgba(22,22,22,.97)}
.col{position:absolute;top:0;height:285px}
.welcome{left:0;width:390px;border-right:1px dotted #444}
.gallery{left:390px;width:604px;background:#141414;border-right:1px dotted #444}
.tweets{left:994px;width:206px}
h2{font-family:"Josefin Sans",sans-serif;font-weight:300;font-size:27px;letter-spacing:1px;color:var(--white)}
.welcome h2{position:absolute;left:31px;top:22px;font-size:28px}
.welcome p{position:absolute;left:32px;top:66px;width:335px;font-size:12.3px;line-height:19.3px;color:#777}
.welcome p .lead{color:var(--light-text)}
.btn{position:absolute;display:inline-block;color:var(--white);font-family:"Josefin Sans",sans-serif;letter-spacing:.5px}
.welcome .btn{left:31px;top:197px;background:var(--teal-dark);font-size:13px;padding:5px 12px 3px}
.gallery h2{position:absolute;left:24px;top:20px}
.gallery .btn{right:24px;top:13px;padding:4px 7px 2px;font-size:12.5px;background:var(--teal);color:#1a3a3e}
.gallery .rule{position:absolute;left:24px;top:58px;width:556px;border-top:2px dotted #444}
.thumb{position:absolute;width:171px;height:86px}
.tweets h2{position:absolute;left:18px;top:23px;font-size:17px;letter-spacing:.8px;white-space:nowrap}
.tweets .bird{position:absolute;right:9px;top:13px}
.tweet{position:absolute;left:18px;width:175px;font-size:10px;line-height:13.7px;color:#666}
.tweet b{display:block;color:var(--white);font-size:11px;margin-bottom:7px}
.tweet em{display:block;font-style:normal;font-weight:700;color:var(--white);font-size:10.5px;margin-top:3px}
.footer-band{position:absolute;left:0;top:891px;width:1200px;height:39px;border-top:2px dotted var(--teal);background:linear-gradient(90deg,#6d6a66,#3a3a36 40%,#2c3a26 75%,#4d4c48)}
.copyright{position:absolute;left:474px;top:902px;width:240px;height:28px;background:#0d0d0d;border-radius:14px 14px 0 0;font-size:12px;color:#ddd;text-align:center;padding-top:7px}
</style>
</head>
<body>
<div class="hero" role="img" aria-label="Wedding bouquet of cream and pink roses on white ceremony chairs, softly blurred garden behind"></div>

<div class="arrow left">
  <svg width="70" height="104" viewBox="0 0 70 104"><path d="M0 0 A52 52 0 0 1 0 104 Z" fill="rgba(120,115,110,.45)"/><path d="M40 16 L10 50 L40 84" fill="none" stroke="#fff" stroke-width="5"/></svg>
</div>
<div class="arrow right">
  <svg width="70" height="104" viewBox="0 0 70 104"><path d="M70 0 A52 52 0 0 0 70 104 Z" fill="rgba(120,115,110,.45)"/><path d="M30 16 L60 50 L30 84" fill="none" stroke="#fff" stroke-width="5"/></svg>
</div>

<div class="topbar">
  <nav class="nav"><span>HOME</span><span class="sep">//</span><span>PRICING</span><span class="sep">//</span><span>PHOTO/VIDEO GALLERY</span><span class="sep">//</span><span>CONTACT</span></nav>
  <div class="social"><i></i><i></i><i></i><i></i><i></i></div>
</div>

<div class="brand-panel">
  <svg class="brand-shape" width="234" height="230" viewBox="0 0 234 230"><path d="M0 0 H234 V206 L118 230 L0 214 Z" fill="#fff"/></svg>
  <div class="brand-dot"></div>
  <div class="brand-name">BRINEWOLF<br>STUDIOS</div>
</div>

<div class="hero-title">
  <div class="main">BRINEWOLF</div>
  <div class="sub">STUDIOS</div>
</div>

<div class="band"></div>

<section class="content">
  <div class="col welcome">
    <h2>WELCOME!</h2>
    <p><span class="lead">Lorem ipsum dolor sit amet, consectetuer adipiscing elit, sed diam nonummy nibh euismod tincidunt ut laoreet dolore</span> magna aliquam erat volutpat. Ut wisi enim ad minim veniam, quis nostrud exerci tation ullamcorper suscipit lobortis nisl ut aliquip ex ea commodo consequat. Duis autem vel eum iriure dolor in hendrerit in vulputate velit.</p>
    <span class="btn">READMORE</span>
  </div>

  <div class="col gallery">
    <h2>GALLERY</h2>
    <span class="btn">VIEW GALLERY</span>
    <div class="rule"></div>
    <div class="thumb" style="left:24px;top:71px;background:linear-gradient(90deg,#a8553a,#b9a48c)" role="img" aria-label="Colourful bridal bouquet"></div>
    <div class="thumb" style="left:216px;top:71px;background:linear-gradient(90deg,#e8e6e0,#d8c4a8)" role="img" aria-label="Bride and groom portrait"></div>
    <div class="thumb" style="left:409px;top:71px;background:linear-gradient(90deg,#6a5a7a,#d8d4dc)" role="img" aria-label="Couple exchanging rings"></div>
    <div class="thumb" style="left:24px;top:170px;background:linear-gradient(180deg,#6a6a40,#e8dc8a)" role="img" aria-label="Table flowers in soft light"></div>
    <div class="thumb" style="left:216px;top:170px;background:linear-gradient(90deg,#a8553a,#b9a48c)" role="img" aria-label="Colourful bridal bouquet"></div>
    <div class="thumb" style="left:409px;top:170px;background:linear-gradient(180deg,#4a4a38,#e8e8e4)" role="img" aria-label="Ceremony chairs with flower posies"></div>
  </div>

  <div class="col tweets">
    <h2>LATEST TWEETS</h2>
    <svg class="bird" width="28" height="28" viewBox="0 0 28 28"><circle cx="14" cy="14" r="12.5" fill="none" stroke="#fff" stroke-width="2"/></svg>
    <div class="tweet" style="top:66px"><b>@marten holloway</b>Lorem ipsum dolor sit amet, consectetuer adipiscing elit, sed diam nonummy nibh e<em>3 hours ago</em></div>
    <div class="tweet" style="top:158px"><b>@elise varna</b>magna aliquam erat volutpat. Ut wisi enim ad minim veniam, quis nostrud exerci tation ullamcorper suscipit lobortis nisl ut aliquip ex ea commodo consequat.<em>3 hours ago</em></div>
  </div>
</section>

<div class="footer-band" role="img" aria-label="Blurred ceremony chairs and greenery"></div>
<div class="copyright">Copyright ©2013 Brinewolf Studios</div>
</body>
</html>
```